New business needs it's first website designed and coded for Wordpress

This is a new website for a new business. The business is called The Remote Tech Expert (TRTE). The business is based across multiple countries with the goal of providing workers in the Philippines opportunities to find work in international companies based in Australia, Singapore and New Zealand. The target market for TRTE is large enterprises (initially in Australia) looking for well legally structured business that knows how to recruit the top IT professionals and ensure that they are happy, all compliance, taxes and legals and professionally done and all services contracts are local to ensure enforceability.

We are looking for 10 pages (6 templates) for the website as follows:
Home
About Us
Services
Work from home full-timers
Work from office full-times
Work from home contractors
Work from office contractors
Careers Job Search
Employers Contact Us
Candidates Register your interest

Target Market(s)

IT Professionals in the Philippines & large enterprises in Australia, Singapore and New Zealand

Industry/Entity Type

IT Recruitment

Coding

Coded - Design and coding required

Number of Pages Required

5+ page

Requirements
Must have
• Please based style off logo file attached.

```html
<!DOCTYPE html>
<html lang="en">
<head>
<meta charset="utf-8">
<title>Services | The Remote Tech Expert</title>
<link rel="stylesheet" href="https://fonts.googleapis.com/css2?family=Michroma&family=Poppins:wght@400;500;600;700&display=swap">
<style>
:root{
  --blue:#0aa2e2;
  --blue-deep:#0189cf;
  --ink:#0b0b0b;
  --navy:#041a2b;
  --grey-bg:#f2f2f2;
  --crumb:#eeeeee;
  --text:#4a4a4a;
  --white:#ffffff;
}
*{box-sizing:border-box;margin:0;padding:0}
html,body{width:1200px;height:2254px;overflow:hidden}
body{font-family:"Poppins",sans-serif;color:var(--ink);background:var(--white);position:relative}
.wrap{position:absolute;left:141px;width:918px}
.display{font-family:"Michroma",sans-serif;letter-spacing:.5px}
.accent{color:var(--blue)}
.brand{font-family:"Poppins",sans-serif;font-weight:700;color:var(--blue);letter-spacing:1px}

/* hero */
.hero{position:absolute;top:0;left:0;width:1200px;height:311px;background:linear-gradient(90deg,#232425 0%,#3c3f43 40%,#8e9398 70%,#c9ccce 100%)}
.hero-photo{position:absolute;right:0;top:0;width:520px;height:311px;background:linear-gradient(90deg,rgba(60,63,67,0),rgba(170,176,181,.6) 50%,rgba(120,130,140,.8))}
.hero .brand{position:absolute;left:141px;top:14px;font-size:36px}
.toplinks{position:absolute;right:139px;top:14px;font-size:10px;color:#eee}
.toplinks span{padding:0 8px}
.toplinks .sep{padding:0}
.toplinks .hl{color:var(--blue);padding-right:0}
.nav{position:absolute;left:341px;top:48px;display:flex;gap:0;font-size:11.5px;color:var(--white)}
.nav a{color:inherit;text-decoration:none;margin-right:34px}
.nav a:last-child{margin-right:0}
.hero-title{position:absolute;left:141px;top:135px;border-left:4px solid var(--blue);padding-left:12px;font-size:33px;line-height:36px;color:var(--white)}
.hero-sub{position:absolute;left:141px;top:189px;width:440px;font-size:14px;line-height:27px;color:var(--white)}
.crumbs{position:absolute;top:311px;left:0;width:1200px;height:38px;background:var(--crumb);font-size:14px;line-height:38px;padding-left:141px}
.crumbs b{color:var(--blue);font-weight:600;margin-left:6px}

/* what we do */
.section-title{text-align:center;font-size:30px;line-height:40px}
.wwd{top:436px}
.cards{position:absolute;top:502px;left:141px;display:flex;gap:23.5px}
.card{width:212px;height:333px;background:var(--white);border-radius:8px;box-shadow:0 2px 10px rgba(0,0,0,.12);overflow:hidden;text-align:center}
.card-img{height:162px}
.card h3{font-size:15px;font-weight:600;line-height:21px;margin:24px 10px 10px}
.card p{font-size:11.5px;line-height:18.5px;color:var(--text);padding:0 14px}
.btn-main{position:absolute;top:871px;left:468px;width:264px;height:44px;background:var(--blue);color:var(--ink);font-size:13.5px;display:flex;align-items:center;justify-content:center;gap:10px}

/* value */
.value{position:absolute;top:1000px;left:0;width:1200px;height:785px;background:var(--grey-bg)}
.vtitle{top:1077px;font-size:31px;line-height:39px}
.diagram{position:absolute;left:0;top:0;width:1200px;height:2254px;pointer-events:none}
.center-disc{position:absolute;left:500px;top:1189px;width:202px;height:202px;border-radius:50%;background:var(--white);box-shadow:0 4px 14px rgba(0,0,0,.1);display:flex;align-items:center;justify-content:center}
.center-disc .brand{font-size:48px}
.vicon{position:absolute;width:68px;height:68px;border-radius:50%;background:var(--blue);border:4px solid var(--white);box-shadow:0 2px 8px rgba(0,0,0,.15);display:flex;align-items:center;justify-content:center}
.vlabel{position:absolute;font-size:15px;font-weight:600;line-height:21px}
.vlabel.r{text-align:right}

/* cta */
.footer{position:absolute;top:1785px;left:0;width:1200px;height:469px;background:var(--navy)}
.cta{position:absolute;top:1633px;left:141px;width:918px;height:289px;border-radius:26px;background:linear-gradient(160deg,#08a6e6,#0193d8);text-align:center}
.cta h2{font-size:32px;line-height:40px;margin-top:60px}
.cta p{font-size:14px;line-height:24px;margin-top:12px}
.cta-btns{display:flex;justify-content:center;gap:18px;margin-top:30px}
.pill{height:45px;border-radius:23px;padding:0 24px;font-size:14px;display:flex;align-items:center;gap:10px;background:var(--navy);color:var(--white)}
.pill.ghost{background:transparent;border:1px solid var(--navy);color:#083b5c}

.footer .brand{position:absolute;left:141px;top:220px;font-size:40px}
.socials{position:absolute;left:141px;top:306px;display:flex;gap:7px}
.socials span{width:29px;height:29px;border-radius:50%;border:1.5px solid var(--white)}
.socials span:first-child{background:var(--blue);border-color:var(--blue)}
.fhead{position:absolute;top:219px;font-size:14px;color:var(--white)}
.fhead::after{content:"";display:block;width:30px;height:2px;background:var(--blue);margin-top:10px}
.links{position:absolute;top:263px;list-style:none;font-size:11px;line-height:26.5px;color:var(--white)}
.links .on{color:var(--blue)}
.contact{position:absolute;left:836px;top:262px;color:var(--white);font-size:11px}
.contact .co{font-family:"Michroma",sans-serif;font-size:11.5px;margin-bottom:6px}
.crow{display:flex;gap:8px;line-height:19px;margin-top:6px}
.crow.phone{font-size:14px;letter-spacing:2px;font-weight:500;margin-top:14px}
.crow.mail{margin-top:14px}
.fline{position:absolute;top:415px;left:141px;width:918px;height:1px;background:rgba(255,255,255,.2)}
.legal{position:absolute;top:437px;left:141px;width:918px;display:flex;justify-content:space-between;font-size:11px;color:var(--white)}
</style>
</head>
<body>

<header class="hero">
  <div class="hero-photo" role="img" aria-label="Office photo of IT professionals reviewing work on a laptop"></div>
  <div class="brand">TRTE</div>
  <div class="toplinks"><span>Careers Job Search</span><span class="sep">|</span><span>Employers Contact Us</span><span class="sep">|</span><span class="hl">Candidates Register Your Interest</span></div>
  <nav class="nav"><a>Home</a><a>About Us</a><a>Services</a><a>WFH Full-timers</a><a>WFO Full-timers</a><a>WFH contractors</a><a>WFO contractors</a></nav>
  <h1 class="hero-title display">SERVICES</h1>
  <p class="hero-sub">The Remote Tech Expert offers unique IT Support Services for IT professionals</p>
</header>
<div class="crumbs">Home &nbsp;&raquo;&nbsp; <b>Services</b></div>

<h2 class="wrap section-title display wwd">WHAT WE <span class="accent">DO</span></h2>
<div class="cards">
  <article class="card"><div class="card-img" role="img" aria-label="Photo of a professional working from home on a laptop" style="background:linear-gradient(135deg,#5b6677,#b9a89a)"></div><h3>Permanent Work from Home IT Professionals</h3><p>Discover full-time &amp; permanent work from home IT support jobs for IT professionals in the Philippines.</p></article>
  <article class="card"><div class="card-img" role="img" aria-label="Photo of a professional on a phone call in an office" style="background:linear-gradient(135deg,#d9dcde,#7d8a7a)"></div><h3>Permanent In-House IT Professionals</h3><p>Discover full-time &amp; in-house office IT support jobs for IT professionals in the Philippines.</p></article>
  <article class="card"><div class="card-img" role="img" aria-label="Photo of colleagues discussing documents in an office" style="background:linear-gradient(135deg,#c9cfd3,#3d3f44)"></div><h3>Contract Work from Home IT Professionals</h3><p>Discover flexible &amp; contract-based work from home IT jobs for IT professionals in the Philippines.</p></article>
  <article class="card"><div class="card-img" role="img" aria-label="Photo of a professional working on a laptop with coffee" style="background:linear-gradient(135deg,#d6dde2,#9c7a62)"></div><h3>Contract In-House IT Professionals</h3><p>Discover flexible &amp; contract-based &amp; in-house office IT support jobs for IT professionals in the Philippines.</p></article>
</div>
<div class="btn-main">Join our TRTE Talent Pool Today! <svg width="18" height="10" viewBox="0 0 18 10"><path d="M0 5h16M12 1l4 4-4 4" fill="none" stroke="#0b0b0b" stroke-width="1.6"/></svg></div>

<section class="value"></section>
<h2 class="wrap section-title display vtitle">EMPLOYEE UNIQUE <span class="accent">VALUE<br>PROPOSITION</span></h2>

<svg class="diagram" viewBox="0 0 1200 2254">
  <path d="M495 1219 A129 129 0 1 0 707 1219" fill="none" stroke="#222" stroke-width="2.5"/>
  <g fill="#fff" stroke="#0aa2e2" stroke-width="2.5">
    <circle cx="495" cy="1219" r="6"/><circle cx="707" cy="1219" r="6"/>
    <circle cx="490" cy="1355" r="6"/><circle cx="712" cy="1355" r="6"/>
    <circle cx="604" cy="1417" r="6"/>
  </g>
</svg>
<div class="center-disc"><span class="brand">TRTE</span></div>

<div class="vicon" style="left:401px;top:1185px"><svg width="34" height="34" viewBox="0 0 34 34" fill="none" stroke="#fff" stroke-width="1.6"><path d="M4 16 17 5l13 11M8 13v16h18V13"/><rect x="13" y="19" width="8" height="10"/></svg></div>
<div class="vicon" style="left:730px;top:1185px"><svg width="34" height="34" viewBox="0 0 34 34" fill="none" stroke="#fff" stroke-width="1.6"><rect x="7" y="4" width="18" height="26" rx="2"/><circle cx="16" cy="15" r="5"/><path d="M11 24h10"/></svg></div>
<div class="vicon" style="left:396px;top:1321px"><svg width="34" height="34" viewBox="0 0 34 34" fill="none" stroke="#fff" stroke-width="1.6"><circle cx="17" cy="10" r="5"/><path d="M8 29c0-6 4-10 9-10s9 4 9 10"/></svg></div>
<div class="vicon" style="left:735px;top:1321px"><svg width="34" height="34" viewBox="0 0 34 34" fill="none" stroke="#fff" stroke-width="1.6"><circle cx="15" cy="15" r="10"/><path d="M5 15h20M15 5c-5 6-5 14 0 20M15 5c5 6 5 14 0 20"/><rect x="19" y="19" width="12" height="9"/></svg></div>
<div class="vicon" style="left:570px;top:1441px"><svg width="34" height="34" viewBox="0 0 34 34" fill="none" stroke="#fff" stroke-width="1.6"><rect x="4" y="14" width="16" height="11" rx="1"/><path d="M2 28h20"/><circle cx="24" cy="10" r="7"/><path d="M17 10h14M24 3v14"/></svg></div>

<div class="vlabel r" style="left:200px;top:1196px;width:176px">Work From Anywhere In The Philippines</div>
<div class="vlabel" style="left:823px;top:1196px;width:220px">International Visa Abroad Opportunities</div>
<div class="vlabel r" style="left:200px;top:1333px;width:171px">Stable Employment With Benefits</div>
<div class="vlabel" style="left:828px;top:1333px;width:230px">Get Hired For An International Job Right Out Of University</div>
<div class="vlabel" style="left:480px;top:1531px;width:250px;text-align:center">Access To International IT Companies And Projects</div>

<footer class="footer">
  <div class="brand">TRTE</div>
  <div class="socials" aria-label="Social media links"><span></span><span></span><span></span><span></span></div>
  <div class="fhead display" style="left:378px">QUICK LINKS</div>
  <ul class="links" style="left:378px"><li class="on">Home</li><li>About Us</li><li>Services</li><li>Work from home full-timers</li><li>Work from office full-times</li></ul>
  <ul class="links" style="left:553px"><li>Work from home contractors</li><li>Work from office contractors</li><li>Careers Job Search</li><li>Employers Contact Us</li><li>Candidates Register your interest</li></ul>
  <div class="fhead display" style="left:836px">CONTACT DETAILS</div>
  <div class="contact">
    <div class="co"><span class="accent">THE REMOTE</span> TECH EXPERT</div>
    <div class="crow"><svg width="12" height="16" viewBox="0 0 12 16"><path d="M6 0a6 6 0 0 0-6 6c0 4.5 6 10 6 10s6-5.5 6-10a6 6 0 0 0-6-6z" fill="#0aa2e2"/><circle cx="6" cy="6" r="2.2" fill="#041a2b"/></svg><span>123, Loream Ipsum Dollar Smit Ametm,<br>Nibh Nonummy. US - 123b 456</span></div>
    <div class="crow phone"><svg width="14" height="14" viewBox="0 0 14 14"><path d="M3 0l3 3-1.5 2a8 8 0 0 0 4.5 4.5L11 8l3 3-2 2.5C6 13 1 8 .5 2z" fill="#0aa2e2"/></svg><span>123 456 7890</span></div>
    <div class="crow mail"><svg width="13" height="10" viewBox="0 0 13 10"><rect width="13" height="10" rx="1" fill="#0aa2e2"/><path d="M1 1l5.5 4.5L12 1" fill="none" stroke="#041a2b" stroke-width="1.2"/></svg><span>info@theremotetechexpert.com</span></div>
  </div>
  <div class="fline"></div>
  <div class="legal"><span>Copyright 2024 The Remote Tech Expert. All Rights Reserved.</span><span>Privacy policy | Terms of service</span></div>
</footer>

<section class="cta">
  <h2 class="display">JOIN OUR TRTE TALENT POOL</h2>
  <p>Explore exciting career opportunities in the IT industry and be a part of a work-life<br>balanced team build for growth, innovation, and success.</p>
  <div class="cta-btns">
    <span class="pill">About Us <svg width="18" height="10" viewBox="0 0 18 10"><path d="M0 5h16M12 1l4 4-4 4" fill="none" stroke="#fff" stroke-width="1.6"/></svg></span>
    <span class="pill ghost">Job Openings <svg width="18" height="10" viewBox="0 0 18 10"><path d="M0 5h16M12 1l4 4-4 4" fill="none" stroke="#083b5c" stroke-width="1.6"/></svg></span>
    <span class="pill">Register <svg width="18" height="10" viewBox="0 0 18 10"><path d="M0 5h16M12 1l4 4-4 4" fill="none" stroke="#fff" stroke-width="1.6"/></svg></span>
  </div>
</section>

</body>
</html>
```